Flyer Design for sewing business

Hi. i need flyers for my new business called " Vora Stitchworks". I am based in Sauchie. I offer Door to Door Clothing Alteration Service!
I provide a door to door alteration service for Clackmannanshire area with 20 miles radiance! (I give free consultations at your preferred location where I can accurately quote the cost of the alteration, as this depends on the garment itself. I aim to deliver the completed item back to you within a week though often it is less than this.)
I also design and sew occasional girls dresses ( first communion, flower girl, party dresses)
The consultation are free with no commitment to take the service.

I wold like see designs that use colors similar to colors on my website, like dusty pink, orange.

To contact either phone MIRA 07912348806
or email: mira.tusk71@quellmail.com

www.brimlink.com/vorastitchworks
www.vora-stitchworks.pagenest.com

THAT IS THE Price List Jeans/Trousers: Shorten....................................from £10.00 Taken in (waist).......................from £8.00 Taken in (side seams)..............from £10.00 Replace zip...............................from £10.00 Dresses/Skirts: Shorten....................................from £10.00 Taken in (waist).......................from £8.00 Taken in (side seams)..............from £8.00 Replace zip...............................from £10.00 Jacket/Coat: Shorten sleeves........................from £12.00 Shorten length (Jacket)...........from £16.00 Shorten length (Coat)..............from £18.00 Taken in (back seam)...............from £12.00 Taken in (side seams)..............from £18.00 Repairs......................................from £5.00 Bridal: Shorten Wedding Dress...........from £25.00 All other bridal alteration quotes can be given on consultation.

Reason: HI, ALL! IN THE NEXT FEW DAYS I GONE EXPERIENCE HOUSE MOVE AND SOME STRESS INVOLVING IN THIS.THANK YOU ALL FOR UNDERSTANDING AND A PATIENCE!

```html
<!DOCTYPE html>
<html lang="en">
<head>
<meta charset="utf-8">
<title>Vora Stitchworks – Flyer</title>
<link rel="stylesheet" href="https://fonts.googleapis.com/css2?family=Playfair+Display+SC:wght@900&family=Open+Sans:wght@700;800&family=Libre+Baskerville&display=swap">
<style>
  :root {
    --mauve: #b97aa6;
    --mauve-light: #d9a9c9;
    --mauve-deep: #9c5f8b;
    --border-strip: #f1d6e4;
    --cream: #f7ead0;
    --ink: #141014;
    --magenta: #ee2fe6;
    --white: #ffffff;
    --logo-frame: #e2789d;
    --bow-pink: #e86fbf;
    --bow-light: #f8b6e0;
    --dress-white: #ecebf2;
    --stair-brown: #8f7268;
    --clips-dark: #0b0a0c;
  }
  * { box-sizing: border-box; margin: 0; padding: 0; }
  html, body { width: 1200px; height: 851px; overflow: hidden; }
  body { font-family: "Open Sans", Arial, sans-serif; }

  .flyer {
    position: relative;
    width: 1200px; height: 851px;
    background: radial-gradient(ellipse at 55% 25%, var(--mauve-light) 0%, var(--mauve) 55%, var(--mauve-deep) 100%);
    overflow: hidden;
  }
  .border-pattern {
    position: absolute; top: 0; height: 851px;
    background: var(--border-strip);
  }
  .border-pattern.left { left: 0; width: 22px; }
  .border-pattern.right { right: 0; width: 34px; }

  .logo-box {
    position: absolute; left: 55px; top: 32px; width: 276px; height: 260px;
    background: var(--white);
    border: 4px solid var(--logo-frame);
    display: flex; align-items: flex-end; justify-content: center; gap: 8px;
    padding-bottom: 30px;
  }
  .logo-box .mark { width: 12px; height: 12px; background: var(--logo-frame); border-radius: 50%; margin-bottom: 6px; }
  .logo-box .name {
    font-family: "Libre Baskerville", Georgia, serif;
    font-size: 18px; color: var(--ink); white-space: nowrap;
  }

  .headline {
    position: absolute; left: 368px; top: 18px; width: 720px;
    font-family: "Playfair Display SC", Georgia, serif; font-weight: 900;
    font-size: 60px; letter-spacing: 2px; color: var(--ink);
    text-shadow: 4px 3px 0 var(--cream);
    text-align: center; white-space: nowrap;
  }
  .tagline {
    position: absolute; left: 380px; top: 89px; width: 710px;
    font-size: 27px; font-weight: 700; color: var(--cream);
    text-align: center; letter-spacing: -0.3px; white-space: nowrap;
  }

  .form-illustration {
    position: absolute; left: 540px; top: 150px; width: 200px; height: 560px;
    background: linear-gradient(180deg, rgba(232,170,210,0.18), rgba(232,170,210,0.06));
    border-radius: 100px 100px 20px 20px;
  }

  .services { position: absolute; left: 36px; top: 320px; list-style: none; }
  .services li {
    display: flex; align-items: flex-start; gap: 6px;
    font-size: 32px; font-weight: 700; color: var(--ink); line-height: 38px;
    margin-bottom: 3px; letter-spacing: -0.5px; white-space: nowrap;
  }
  .services li svg { flex: none; margin-top: 9px; }
  .services .sub { display: block; }

  .photo { position: absolute; box-shadow: 0 0 18px rgba(255,235,245,0.9); }
  .photo.bow {
    left: 823px; top: 148px; width: 297px; height: 160px;
    background:
      radial-gradient(ellipse 45% 55% at 52% 45%, var(--bow-light), transparent 70%),
      linear-gradient(180deg, #f3c3df 0%, var(--bow-pink) 35%, #d85aaa 70%, #f0a6d4 100%);
  }
  .photo.dress {
    left: 823px; top: 310px; width: 297px; height: 370px;
    background:
      radial-gradient(ellipse 50% 40% at 45% 68%, var(--dress-white), transparent 75%),
      radial-gradient(ellipse 25% 22% at 42% 38%, #f4f2f8, transparent 80%),
      linear-gradient(100deg, var(--stair-brown) 0%, #a98c82 45%, #cfc6c4 80%, #e6e2e0 100%);
  }

  .clips-promo {
    position: absolute; left: 60px; top: 498px; width: 297px; height: 224px;
    background:
      radial-gradient(circle at 45% 42%, rgba(236,150,180,0.55), transparent 18%),
      radial-gradient(circle at 28% 82%, rgba(120,140,210,0.55), transparent 18%),
      radial-gradient(circle at 72% 62%, rgba(235,230,205,0.45), transparent 18%),
      radial-gradient(circle at 20% 55%, rgba(200,210,180,0.4), transparent 14%),
      var(--clips-dark);
  }
  .clips-promo p {
    color: var(--white); font-family: Arial, sans-serif; font-weight: 400;
    font-size: 16px; text-align: center; margin-top: 14px; line-height: 1.25;
    margin-left: -12px;
  }

  .dress-occasions {
    position: absolute; left: 350px; top: 592px; width: 500px;
    text-align: center; color: var(--cream); font-size: 28px; font-weight: 700;
    line-height: 28px; letter-spacing: 0.3px; white-space: nowrap;
  }

  .call-line {
    position: absolute; left: 288px; top: 686px; width: 620px; text-align: center;
    font-size: 40px; font-weight: 800; color: var(--magenta); letter-spacing: 2px;
    -webkit-text-stroke: 1px #4a0f48;
    text-shadow: 3px 3px 0 rgba(40,10,40,0.55); white-space: nowrap;
  }
  .contact-line {
    position: absolute; left: 150px; top: 734px; width: 900px; text-align: center;
    font-size: 22px; font-weight: 700; color: var(--cream); white-space: nowrap;
  }

  .web-banner {
    position: absolute; left: 170px; top: 782px; width: 860px; height: 60px;
    background: linear-gradient(180deg, #d98cbf, #c876ad);
    display: flex; align-items: center; justify-content: center;
  }
  .web-banner span {
    font-size: 33px; font-weight: 800; color: var(--cream); letter-spacing: 2px;
    white-space: nowrap;
  }
</style>
</head>
<body>
<main class="flyer">
  <div class="border-pattern left" role="img" aria-label="Decorative floral border pattern"></div>
  <div class="border-pattern right" role="img" aria-label="Decorative floral border pattern"></div>

  <div class="form-illustration" role="img" aria-label="Faint line drawing of a dressmaker's wire mannequin"></div>

  <div class="logo-box">
    <span class="mark"></span>
    <span class="name">VORA STITCHWORKS</span>
  </div>

  <h1 class="headline">VORA STITCHWORKS</h1>
  <p class="tagline">Handmade Flower Girls Dresses &amp; Occasional Dresses</p>

  <ul class="services">
    <li><svg width="22" height="20" viewBox="0 0 22 20"><path d="M2 18 L18 3 M12 3 L19 2 L18 9" stroke="#f7ead0" stroke-width="3" fill="none" stroke-linecap="round"/></svg>
      <span>Door to Door Clothing Alteration Service<span class="sub">Clackmannanshire area</span></span></li>
    <li><svg width="22" height="20" viewBox="0 0 22 20"><path d="M2 18 L18 3 M12 3 L19 2 L18 9" stroke="#f7ead0" stroke-width="3" fill="none" stroke-linecap="round"/></svg>
      <span>Free consultations at your preferred location</span></li>
    <li><svg width="22" height="20" viewBox="0 0 22 20"><path d="M2 18 L18 3 M12 3 L19 2 L18 9" stroke="#f7ead0" stroke-width="3" fill="none" stroke-linecap="round"/></svg>
      <span>Delivery of completed item&nbsp; within a week or less</span></li>
  </ul>

  <div class="photo bow" role="img" aria-label="Close-up photo of a pink satin bow with a jewelled brooch on a girl's dress"></div>
  <div class="photo dress" role="img" aria-label="Photo of a girl in a white tulle party dress with a lilac ribbon sash, standing by carpeted stairs"></div>

  <div class="clips-promo" role="img" aria-label="Photo of fabric rose and bow crocodile hair clips on a black background">
    <p>INTRODUCING:<br>CROCODILE CLIPS</p>
  </div>

  <p class="dress-occasions">For&nbsp; Occasional Girls Dresses:<br>First Communion,<br>Fower Girl &amp; Party Dresses</p>

  <p class="call-line">CALL MIRA @ 0791.234.8806</p>
  <p class="contact-line">mira.tusk71@quellmail.com | www.brimlink.com/vorastitchworks</p>

  <div class="web-banner"><span>WWW.VORA-STITCHWORKS.PAGENEST.COM</span></div>
</main>
</body>
</html>
```